Brixom Vale needs a powerpoint design

We need a powerpoint design for an Information Technology based in Fairfax call "Brixom Vale". We are Information Technology solutions provider for the Federal Government. We develop Talvex, Mobile and Cloud based solutions. We support the Healthcare and Financial sectors of the Government. We would like to see designs that use the colors of our logo. We've attached a copy of our logo. The final design should communicate Information Technology and System Integration with Agile Development.

Target Market(s)

Our target market is the Federal Government and System Integators in the Washington DC area.

Industry/Entity Type

Government

Requirements
Must have
• The powerpoint design must have a professional look.

```html
<!DOCTYPE html>
<html lang="en">
<head>
<meta charset="utf-8">
<title>Brixom Vale – Project Slide</title>
<link href="https://fonts.googleapis.com/css2?family=Open+Sans:wght@400;600;700&display=swap" rel="stylesheet">
<style>
  :root {
    --navy: #0a3a9c;
    --navy-deep: #062a7a;
    --royal: #1456c8;
    --bright: #0b56dc;
    --sky: #9fbaf9;
    --line: #2aa3e8;
    --grey-light: #c0c0c0;
    --grey-mid: #7f7f7f;
    --grey-dark: #595959;
    --ink: #1a1a1a;
    --heading-blue: #1f4fb5;
    --white: #ffffff;
  }
  * { margin: 0; padding: 0; box-sizing: border-box; }
  html, body { width: 1200px; height: 900px; overflow: hidden; background: var(--white); }
  body { font-family: "Open Sans", Arial, sans-serif; }
  .slide { position: relative; width: 1200px; height: 900px; overflow: hidden; background: var(--white); }

  .header {
    position: absolute; left: 0; top: 0; width: 1200px; height: 117px;
    background: linear-gradient(90deg, var(--navy-deep) 0%, var(--navy) 45%, var(--royal) 100%);
    border-bottom: 4px solid var(--line);
  }
  .header-texture {
    position: absolute; right: 0; top: 0; width: 480px; height: 113px;
    background: linear-gradient(100deg, rgba(20,86,200,0) 0%, rgba(90,150,235,0.55) 55%, rgba(160,200,250,0.7) 100%);
  }
  .slide-title {
    position: absolute; left: 57px; top: 32px;
    color: var(--white); font-weight: 700; font-size: 41px; letter-spacing: 0.5px;
  }
  .title-tab { position: absolute; left: 57px; top: 90px; }

  .lead {
    position: absolute; left: 57px; top: 158px; width: 1090px;
    color: var(--heading-blue); font-weight: 700; font-size: 24px; line-height: 41px;
  }

  .chart { position: absolute; left: 0; top: 0; }
  .slice-label { font-family: "Open Sans", Arial, sans-serif; font-weight: 700; font-size: 16.5px; }
  .on-dark { fill: var(--white); }
  .on-light { fill: var(--ink); }

  .footer-rule { position: absolute; left: 0; top: 786px; width: 1200px; height: 6px; background: var(--line); }
  .footer {
    position: absolute; left: 0; top: 795px; width: 1200px; height: 105px;
    background: linear-gradient(90deg, var(--navy-deep) 0%, var(--navy) 50%, var(--royal) 100%);
  }
  .page-badge {
    position: absolute; left: 39px; top: 828px; width: 42px; height: 42px;
    transform: rotate(45deg); border-radius: 6px;
    background: var(--royal); border: 2px solid #3f7fe6;
  }
  .page-number {
    position: absolute; left: 39px; top: 834px; width: 42px; text-align: center;
    color: var(--white); font-weight: 700; font-size: 19px;
  }
  .copyright {
    position: absolute; left: 116px; top: 835px;
    color: var(--white); font-size: 19px;
  }
  .brand {
    position: absolute; right: 22px; top: 822px; display: flex; align-items: center; gap: 16px;
  }
  .brand-mark { width: 48px; height: 48px; background: var(--white); }
  .brand-name { color: var(--white); font-weight: 700; font-size: 42px; line-height: 1; }
</style>
</head>
<body>
<div class="slide">
  <header class="header">
    <div class="header-texture" role="img" aria-label="Decorative binary digit pattern fading across the header"></div>
    <h1 class="slide-title">PROJECT TITLE HERE</h1>
  </header>
  <svg class="title-tab" width="36" height="62" viewBox="0 0 36 62" aria-hidden="true">
    <polygon points="0,0 36,0 36,26 0,62" fill="#1e3fa8"/>
  </svg>

  <p class="lead">Lorem ipsum dolor sit ipsum Lorem ipsum dolor sit ipsum Lorem ipsum Lorem ipsum dolor sit ipsum Lorem ipsum dolor sit ipsum Lorem ipsum</p>

  <svg class="chart" width="1200" height="900" viewBox="0 0 1200 900" role="img" aria-label="Pie chart with six segments">
    <g stroke="#ffffff" stroke-width="2" stroke-linejoin="round">
      <path d="M558 512 L558 281 A231 231 0 0 1 692.1 323.9 Z" fill="var(--grey-light)"/>
      <path d="M558 512 L692.1 323.9 A231 231 0 0 1 777.1 585.3 Z" fill="var(--sky)"/>
      <path d="M558 512 L777.1 585.3 A231 231 0 0 1 640.8 727.7 Z" fill="var(--bright)"/>
      <path d="M558 512 L640.8 727.7 A231 231 0 0 1 339.6 587.2 Z" fill="var(--navy)"/>
      <path d="M558 512 L339.6 587.2 A231 231 0 0 1 430.2 319.6 Z" fill="var(--grey-dark)"/>
      <path d="M558 512 L430.2 319.6 A231 231 0 0 1 558 281 Z" fill="var(--grey-mid)"/>
    </g>
    <circle cx="558" cy="512" r="40" fill="var(--navy)" stroke="#ffffff" stroke-width="4"/>

    <text class="slice-label on-light" text-anchor="middle">
      <tspan x="603" y="347">Lorem</tspan><tspan x="603" y="371">ipsum</tspan><tspan x="603" y="395">dolor</tspan>
    </text>
    <text class="slice-label on-dark" text-anchor="middle">
      <tspan x="514" y="347">Lorem</tspan><tspan x="514" y="371">ipsum</tspan><tspan x="514" y="395">dolor</tspan>
    </text>
    <text class="slice-label on-light" text-anchor="middle">
      <tspan x="696" y="479">Lorem ipsum</tspan><tspan x="696" y="503">dolor</tspan>
    </text>
    <text class="slice-label on-dark" text-anchor="middle">
      <tspan x="430" y="472">Lorem ipsum dolor</tspan><tspan x="430" y="496">Lorem ipsum dolor</tspan>
    </text>
    <text class="slice-label on-dark" text-anchor="middle">
      <tspan x="667" y="605">Lorem ipsum</tspan><tspan x="663" y="629">dolor</tspan>
    </text>
    <text class="slice-label on-dark" text-anchor="middle">
      <tspan x="494" y="619">Lorem ipsum dolor</tspan><tspan x="494" y="643">Lorem ipsum dolor</tspan>
    </text>
  </svg>

  <div class="footer-rule"></div>
  <footer class="footer"></footer>
  <div class="page-badge"></div>
  <div class="page-number">01</div>
  <div class="copyright">Copyright text here</div>
  <div class="brand">
    <span class="brand-mark"></span>
    <span class="brand-name">Brixom Vale</span>
  </div>
</div>
</body>
</html>
```